Business Card Design

I do estate sales and would like business card to reflect look and feel of attached logo. I also have copy of logo in .eps and .tif if you need that instead of .jpeg.
Updates

sorry for the delay in reviewing these designs. I will pick one by tomorrow. Here are the absolutes: *must have tagline (we find good homes for your treasures *must use blue and green *must be horizontal *nothing too fancy please submit your best and final. Thanks so much!

Industry/Entity Type

Business

Contact Information for Business Card

Mira Tolland

TAGS by MIRA
We find good homes for your treasures.

Specializing in one to three-day sales
o (no sale too big or too small)
• Home and garage organizing
• Home Clean-out

Call Mira Tolland at 202-555-0147
to schedule.

```html
<!DOCTYPE html>
<html lang="en">
<head>
<meta charset="utf-8">
<title>TAGS by MIRA – Business Card</title>
<link rel="stylesheet" href="https://fonts.googleapis.com/css2?family=Encode+Sans:wght@300;400&display=swap">
<style>
  :root {
    --brand-blue: #0a7ba2;
    --brand-green: #6f8a33;
    --edge-grey: #c6c6c6;
    --ink: #2a2a2a;
    --paper: #ffffff;
    --on-color: #ffffff;
  }
  * { margin: 0; padding: 0; box-sizing: border-box; }
  html, body {
    width: 1200px; height: 741px; overflow: hidden;
    background: var(--paper);
  }
  .card {
    position: relative;
    width: 1200px; height: 741px;
    background: var(--paper);
    font-family: "Encode Sans", sans-serif;
    font-weight: 300;
    overflow: hidden;
  }
  .brand-name {
    position: absolute;
    top: 120px; left: 0; width: 1200px;
    text-align: center;
    font-size: 92px;
    font-weight: 400;
    letter-spacing: 4px;
    color: var(--brand-green);
    line-height: 1;
  }
  .tagline {
    position: absolute;
    top: 311px; left: 0; width: 1200px;
    text-align: center;
    font-size: 39px;
    letter-spacing: 1px;
    color: var(--ink);
    line-height: 1;
  }
  .roof {
    position: absolute; left: 0; top: 0;
    width: 1200px; height: 741px;
  }
  .roof .edge { fill: var(--edge-grey); }
  .roof .left-panel { fill: var(--brand-blue); }
  .roof .right-panel { fill: var(--brand-green); }
  .roof .bullet { stroke: var(--on-color); stroke-width: 7; stroke-linecap: round; }
  .contact {
    position: absolute;
    right: 635px; top: 540px;
    text-align: right;
    color: var(--on-color);
    font-size: 28px;
    line-height: 35px;
  }
  .services {
    position: absolute;
    left: 639px; top: 540px;
    list-style: none;
    color: var(--on-color);
    font-size: 28px;
    line-height: 35px;
  }
</style>
</head>
<body>
  <main class="card">
    <h1 class="brand-name">TAGS by MIRA</h1>
    <p class="tagline">WE FIND GOOD HOMES FOR YOUR TREASURES</p>

    <svg class="roof" viewBox="0 0 1200 741" aria-hidden="true">
      <polygon class="edge" points="0,503 600,386 1200,503 1200,741 0,741"/>
      <polygon class="left-panel" points="0,519 600,395 600,741 0,741"/>
      <polygon class="right-panel" points="600,395 1200,519 1200,741 600,741"/>
      <line class="bullet" x1="587" y1="556" x2="613" y2="556"/>
      <line class="bullet" x1="587" y1="626" x2="613" y2="626"/>
      <line class="bullet" x1="587" y1="661" x2="613" y2="661"/>
    </svg>

    <p class="contact">Call Mira Tolland<br>at 202-555-0147 to schedule</p>

    <ul class="services">
      <li>Specializing in one to three-day sales<br>(no sale too big or too small)</li>
      <li>Home and garage organizing</li>
      <li>Home Clean-out</li>
    </ul>
  </main>
</body>
</html>
```